Cork Lantern website design elements

Company: Cork Lantern
Business: Wine website (selling wine online)
www.corklantern-demo.com.au
Please note that this is an initial project, ongoing design work will be required after this project.
Design requirement
Note: Full website design not required, only specific elements to enhance current design.
- Must work with existing logo and wood background (do not change site background)
- Must work with a orange (please improve current orange colour) and blue colour (blue colour in attachments)
- Pictures of wine bottles or wine glasses are not to be used in design elements.
I currently have an existing design which I would like certain elements designed for. Design elements must work with responsive functionality.
I am trying to achieve a modern retro feel of the website, please refer to the below websites as examples that I am trying to look like.
- https://au.brisktrimhouse-demo.com/
- http://www.kestrelmarlow-demo.com/italian/australia/home
- http://www.tangerinefizz-demo.co.uk/
- http://www.codeharbour-demo.org.nz/13/
As mentioned the site is already built and I need certain elements to work with what is already there. All elements must work with current logo and wood panel background.
I require the following elements
• Menu bar (must be the orange)
• Home page promo slider (Text, this weeks special etc)
• 2x homepage promo tabs buttons (Join the lantern club, what's in the box deal)
• 4x Homepage navigation tabs (Red wine, White wine, Sparkling, Pre mixed cases)
• Add to cart button
• Product image backdrop (can be wider than current examples)
o I would like the backdrops to be a different colour scheme to each other e.g red wine will habe red colour, white will have a cream colour, etc)
o I would prefer a close up of the product, does not need to be full view
Please refer to attachments for elements that I like and would like to mimic.
Colour scheme
- Use existing orange (please suggest if you think of a better tone)
- Secondary colour light baby blue (suggest best options)
- Please advise of other colours needed
Design elements to be provided in jog and raw design format.
This project will require ongoing work.
I will provide access details to site upon request.
Please contact me if you have any questions.
Tobias
Cork Lantern

```html
<!DOCTYPE html>
<html lang="en">
<head>
<meta charset="utf-8">
<title>Cork Lantern</title>
<link href="https://fonts.googleapis.com/css2?family=Open+Sans:wght@300;400;600&display=swap" rel="stylesheet">
<style>
:root{
  --wood-dark:#7a4a22;
  --wood-mid:#a8693a;
  --wood-light:#c48a52;
  --orange:#f08a0c;
  --orange-deep:#ec6f0a;
  --orange-text:#ee6c12;
  --red-tile:#e4484e;
  --cream-tile:#f5e6cc;
  --blue-tile:#6dd9ef;
  --ink:#2d2d2d;
  --body-text:#555;
  --muted:#b5b5b5;
  --line:#dcdcdc;
  --white:#fff;
  --dark-btn:#2a2522;
}
*{box-sizing:border-box;margin:0;padding:0}
html,body{width:1158px;height:1200px;overflow:hidden}
body{
  position:relative;
  font-family:"Open Sans",Arial,sans-serif;
  background:
    repeating-linear-gradient(180deg,rgba(60,30,10,.0) 0 95px,rgba(60,30,10,.35) 95px 98px,rgba(255,220,170,.08) 98px 100px),
    linear-gradient(90deg,var(--wood-mid),var(--wood-light) 30%,var(--wood-mid) 55%,var(--wood-light) 80%,var(--wood-mid));
}
.abs{position:absolute}
.brand{left:118px;top:50px;display:flex;align-items:center;gap:10px;color:var(--white);font-size:24px;font-weight:600}
.brand-dot{width:18px;height:18px;border-radius:50%;background:var(--white)}
.cart-btn{left:674px;top:27px;width:137px;height:31px;background:var(--orange);color:var(--white);font-size:13px;display:flex;align-items:center;justify-content:center;gap:8px;letter-spacing:.3px}
.search{left:820px;top:27px;width:212px;height:31px;background:#f1f1f1;display:flex;align-items:center;justify-content:space-between;padding:0 8px 0 10px;font-size:12px;font-style:italic;color:#777}
.promo-btn{top:91px;height:37px;border:2px solid #111;outline:1px solid #5a4a3e;background:var(--dark-btn);color:var(--white);font-size:15px;display:flex;align-items:center;justify-content:center;letter-spacing:.3px;white-space:nowrap}
.club{left:644px;width:176px}
.box-deal{left:834px;width:199px}
.page{left:125px;top:139px;width:907px;height:987px;background:var(--white);box-shadow:0 0 6px rgba(0,0,0,.4)}
.menu{left:116px;top:157px;width:926px;height:54px;background:linear-gradient(180deg,var(--orange),var(--orange-deep));box-shadow:0 4px 6px rgba(0,0,0,.25);display:flex;justify-content:center;align-items:center;gap:20px;color:var(--white);font-size:19px;font-weight:600;letter-spacing:.5px}
.menu .sep{font-weight:400}
.hero{left:137px;top:223px;width:885px;height:380px;border:3px solid #ececec;background:var(--white);overflow:hidden}
.hero-photo{position:absolute;right:0;top:0;width:450px;height:100%;background:radial-gradient(circle at 60% 45%,#8a1a24 0,#5e1018 18%,#c9c9cc 40%,#efefef 70%)}
.hero h1{position:absolute;left:22px;top:122px;font-size:42px;font-weight:600;color:var(--orange-text);letter-spacing:.5px;white-space:nowrap;z-index:1}
.hero p{position:absolute;left:23px;top:180px;width:410px;font-size:15px;line-height:22px;color:var(--ink)}
.dots{position:absolute;left:24px;top:356px;display:flex;gap:7px}
.dots span{width:13px;height:13px;border-radius:50%;background:#bbb}
.dots span:first-child{background:#444}
.tile{top:633px;width:277px;height:120px;display:flex;padding:18px 0 0 30px;gap:28px}
.tile h2{font-size:20px;font-weight:400;white-space:nowrap}
.tile small{display:block;margin-top:38px;font-size:12px;font-weight:600;white-space:nowrap}
.t-red{left:137px;background:var(--red-tile);color:var(--white)}
.t-white{left:441px;background:var(--cream-tile);color:var(--ink)}
.t-spark{left:745px;background:var(--blue-tile);color:var(--ink)}
.card{top:780px;height:225px;border:1px solid var(--line);background:var(--white);padding:12px 19px}
.card h3{position:relative;z-index:1;font-size:24px;font-weight:400;color:var(--ink);white-space:nowrap}
.card p{position:relative;z-index:1;font-size:11.5px;line-height:23px;color:var(--body-text);margin-top:6px;letter-spacing:.2px}
.card .more{position:absolute;z-index:1;left:17px;bottom:18px;font-size:23px;font-weight:300;color:var(--muted);letter-spacing:.5px}
.welcome{left:137px;width:587px}
.products{left:743px;width:279px;overflow:hidden}
.products p{width:120px;line-height:20px}
.bottles{position:absolute;right:0;bottom:0;width:150px;height:172px;background:linear-gradient(100deg,rgba(255,255,255,0) 0,rgba(255,255,255,0) 8%,#6b1a22 38%,#2d1a14 60%,#7a6a3a 78%,#c9c2b8)}
.newsletter{left:137px;top:1020px;width:885px;height:95px;background:var(--orange)}
.newsletter h4{position:absolute;left:29px;top:31px;color:var(--white);font-size:23px;font-weight:400;letter-spacing:.3px;white-space:nowrap;line-height:30px}
.email{position:absolute;left:286px;top:25px;width:429px;height:46px;background:var(--white);border:2px solid #e8e8e8;font-size:15px;color:#888;display:flex;align-items:center;padding-left:15px}
.signup{position:absolute;left:730px;top:25px;width:121px;height:46px;background:linear-gradient(#3a3a3a,#1f1f1f);color:var(--white);font-size:17px;display:flex;align-items:center;justify-content:center;letter-spacing:.5px}
.copyright{left:125px;top:1155px;font-size:12px;color:var(--white);font-weight:600;letter-spacing:.2px}
.social{left:869px;top:1145px;display:flex;gap:7px}
.social span{width:37px;height:37px;border-radius:50%;background:var(--white)}
</style>
</head>
<body>
<div class="abs brand"><span class="brand-dot"></span>Cork Lantern</div>

<div class="abs cart-btn">
  <svg width="20" height="16" viewBox="0 0 20 16"><path d="M1 5h18l-2 10H3z" fill="#fff"/><path d="M6 5l4-4 4 4" stroke="#fff" stroke-width="2" fill="none"/></svg>
  ADD TO CART
</div>
<div class="abs search">Search...
  <svg width="24" height="22" viewBox="0 0 24 22"><circle cx="9" cy="9" r="6.5" stroke="#111" stroke-width="2.5" fill="none"/><path d="M14 14l7 6" stroke="#111" stroke-width="3.5" stroke-linecap="round"/></svg>
</div>
<div class="abs promo-btn club">Join the Lantern Club</div>
<div class="abs promo-btn box-deal">What's in the Box Deal</div>

<div class="abs page"></div>
<nav class="abs menu">
  <span>HOME</span><span class="sep">|</span><span>RED WINE</span><span class="sep">|</span><span>WHITE WINE</span><span class="sep">|</span><span>SPARKLING</span><span class="sep">|</span><span>MIXED CASES</span>
</nav>

<section class="abs hero">
  <div class="hero-photo" role="img" aria-label="Photo of a red wine bottle in a metal ring holder beside a glass of red wine"></div>
  <h1>THIS WEEKS SPECIAL</h1>
  <p>Aliquam molestie, mi et imperdiet euismod, dui purus auctor tellus, et interdum lacus lectus et ante.</p>
  <div class="dots"><span></span><span></span><span></span><span></span></div>
</section>

<a class="abs tile t-red">
  <svg width="46" height="92" viewBox="0 0 46 92"><path d="M4 2Q0 30 23 44Q46 30 42 2" stroke="#fff" stroke-width="3" fill="none"/><path d="M3 22Q20 17 43 20Q40 38 23 44Q6 38 3 22z" fill="#fff"/><path d="M23 44v40M9 88h28" stroke="#fff" stroke-width="4"/></svg>
  <div><h2>Red Wine</h2><small>See All Red Wine &gt;&gt;</small></div>
</a>
<a class="abs tile t-white">
  <svg width="46" height="92" viewBox="0 0 46 92"><path d="M6 2h34q4 30-17 44Q2 32 6 2z" stroke="#111" stroke-width="2.5" fill="#fff"/><path d="M6 2h34l2 20H4z" fill="#111"/><path d="M23 46v38M9 88h28" stroke="#111" stroke-width="4"/></svg>
  <div><h2>White Wine</h2><small>See All White Wine &gt;&gt;</small></div>
</a>
<a class="abs tile t-spark">
  <svg width="46" height="92" viewBox="0 0 46 92"><path d="M12 2h22l-6 58h-10z" fill="#fff"/><path d="M23 60v24M11 88h24" stroke="#fff" stroke-width="4"/></svg>
  <div><h2>Sparkling Wine</h2><small>See All Sparkling Wine &gt;&gt;</small></div>
</a>

<section class="abs card welcome">
  <h3>Welcome to Our Website</h3>
  <p>Aliquam molestie, mi et imperdiet euismod, dui purus auctor tellus, et interdum lacus lectus et ante. Sed accumsan sollicitudin sapien, sit amet adipiscing turpis gravida ac. In congue, neque ac lobortis volutpat, libero mauris varius mi, vitae suscipit ipsum ligula vitae risus. Duis aliquam nibh a dui iaculis viverra id a velit. Vivamus egestas risus in magna varius commodo. Sed semper viverra egestas. Etiam pretium porttitor lectus, vel ornare neque porta volutpat.</p>
  <span class="more">LEARN MORE</span>
</section>
<section class="abs card products">
  <div class="bottles" role="img" aria-label="Photo of a row of wine bottles"></div>
  <h3>Our Products</h3>
  <p>Aliquam molestie, mi et imperdiet euismod, dui purus auctor tellus, et interdum lacus lectus et ante.</p>
  <span class="more">VIEW ALL</span>
</section>

<section class="abs newsletter">
  <h4>Newsletter Subscribe</h4>
  <div class="email">Enter Email Address</div>
  <div class="signup">SIGN UP</div>
</section>

<footer>
  <p class="abs copyright">Copyright © 2013. Cork Lantern. All Right Reserved</p>
  <div class="abs social"><span></span><span></span><span></span><span></span></div>
</footer>
</body>
</html>
```